Business Card Design Project

We need a Business Card for an Mechanical Engineering firm in Singapore. The design should be Modern & Technical looking, yet eye catching.

Our company deals in Cutting Tools & Machine Accessories for the Manufacturing Industries such as Oil & Gas, Aero Space, etc... For more information on our Company, you can either email me or view our website www.valtrion.com.sg.

We are trying to revamp our image to give our consumers a fresh new perspective to our company, so we welcome all ideas.

Industry/Entity Type

Business

Requirements
Must have
• Must incorporate New Company Logo into the card as shown in Uploaded file.

```html
<!DOCTYPE html>
<html lang="en">
<head>
<meta charset="utf-8">
<title>Valtrion Tools – Business Card</title>
<link rel="stylesheet" href="https://fonts.googleapis.com/css2?family=Arimo:wght@400;700&display=swap">
<style>
  :root {
    --maroon: #9a1935;
    --rose: #c89391;
    --paper: #edebea;
    --ink: #161616;
    --stage: #e4e2df;
    --white: #ffffff;
  }
  * { margin: 0; padding: 0; box-sizing: border-box; }
  html, body { width: 1200px; height: 900px; overflow: hidden; }
  body {
    background: var(--stage);
    font-family: "Arimo", Arial, sans-serif;
    position: relative;
  }
  .card {
    position: absolute;
    top: 295px;
    width: 540px;
    height: 310px;
    overflow: hidden;
    box-shadow: 0 6px 18px rgba(0,0,0,0.18);
  }
  /* ---------- front ---------- */
  .card-front { left: 40px; background: var(--paper); }
  .front-accent {
    position: absolute;
    left: 110px; top: -90px;
    width: 170px; height: 170px;
    border-radius: 50%;
    background: var(--rose);
    opacity: 0.75;
  }
  .front-band {
    position: absolute;
    left: 0; right: 0; bottom: 0;
    height: 42px;
    background: var(--maroon);
  }
  .contact {
    position: absolute;
    left: 36px; top: 52px;
    color: var(--ink);
    font-size: 11.5px;
    line-height: 1.45;
  }
  .contact-name {
    font-size: 22px;
    font-weight: 700;
    padding-bottom: 6px;
    border-bottom: 1.5px solid var(--white);
    margin-bottom: 8px;
    width: 190px;
  }
  .contact-row { display: flex; align-items: center; gap: 7px; }
  .contact-row svg { width: 10px; height: 10px; flex: none; }
  .contact-group { padding-bottom: 6px; margin-bottom: 6px; border-bottom: 1.5px solid var(--white); }
  .contact-company { font-weight: 700; }
  .brand {
    position: absolute;
    display: flex;
    align-items: center;
    gap: 10px;
    color: var(--maroon);
    font-weight: 700;
    letter-spacing: 0.5px;
  }
  .brand-dot {
    width: 18px; height: 18px;
    border-radius: 50%;
    background: var(--maroon);
    flex: none;
  }
  .card-front .brand { right: 40px; top: 126px; font-size: 28px; }
  /* ---------- back ---------- */
  .card-back { left: 620px; background: var(--maroon); }
  .back-web-panel {
    position: absolute;
    left: 0; top: 0;
    width: 270px; height: 170px;
    background: var(--paper);
    border-bottom-right-radius: 26px;
    padding: 0 14px 14px 0;
  }
  .back-web-inner {
    width: 100%; height: 100%;
    background: var(--rose);
    border-bottom-right-radius: 20px;
    color: var(--white);
    font-size: 12px;
    padding: 34px 0 0 70px;
  }
  .back-logo-panel {
    position: absolute;
    right: 0; top: 85px;
    width: 250px; height: 140px;
    background: var(--paper);
    border-top-left-radius: 26px;
    border-bottom-left-radius: 0;
  }
  .card-back .brand { left: 22px; top: 52px; font-size: 23px; }
</style>
</head>
<body>

<section class="card card-front" aria-label="Business card front">
  <div class="front-accent"></div>
  <div class="front-band"></div>

  <div class="contact">
    <div class="contact-name">Marianne</div>
    <div class="contact-group">
      <div class="contact-row">
        <svg viewBox="0 0 10 10"><circle cx="5" cy="5" r="5" fill="#8a8a8a"/><rect x="3.5" y="2" width="3" height="6" rx="1" fill="#fff"/></svg>
        <span>Tel: 65-61234570</span>
      </div>
      <div class="contact-row">
        <svg viewBox="0 0 10 10"><circle cx="5" cy="5" r="5" fill="#8a8a8a"/><rect x="2.5" y="3" width="5" height="4" fill="#fff"/></svg>
        <span>Fax: 65-61234571</span>
      </div>
      <div class="contact-row">
        <svg viewBox="0 0 10 10"><circle cx="5" cy="5" r="5" fill="#8a8a8a"/><path d="M2.5 3.5h5v3h-5z M2.5 3.5l2.5 2 2.5-2" fill="none" stroke="#fff" stroke-width="0.9"/></svg>
        <span>Email: hello@valtrion.com.sg</span>
      </div>
    </div>
    <div class="contact-group">
      <div class="contact-row">
        <svg viewBox="0 0 10 10"><circle cx="5" cy="5" r="5" fill="#333"/><path d="M5 2l3 2.5v3.5h-6v-3.5z" fill="#fff"/></svg>
        <span class="contact-company">Valtrion Tools Pte Ltd</span>
      </div>
      <div style="padding-left:17px">28 Kallang Way #03-12, Kallang Tech Hub,<br>Singapore 349250</div>
    </div>
    <div class="contact-row">
      <svg viewBox="0 0 10 10"><circle cx="5" cy="5" r="5" fill="#333"/><circle cx="5" cy="5" r="2.6" fill="none" stroke="#fff" stroke-width="0.9"/></svg>
      <span>Website: www.valtrion.com.sg</span>
    </div>
  </div>

  <div class="brand"><span class="brand-dot"></span>Valtrion Tools</div>
</section>

<section class="card card-back" aria-label="Business card back">
  <div class="back-web-panel">
    <div class="back-web-inner">Website: www.valtrion.com.sg</div>
  </div>
  <div class="back-logo-panel">
    <div class="brand"><span class="brand-dot"></span>Valtrion Tools</div>
  </div>
</section>

</body>
</html>
```